Harbor Nightclub

Nightclub flyer., digital single sided, for KV and PX. I included samples of some previous flyers we've used. Sample Info:
HARBOR
FRIDAYS
FRI MAY 1 2020
DJ VORTAN (club floor)
DJ RUZO & DJ TAV (residents on the lounge floor)
4217 Marlow Avenue Sacramento
www.harborvenuehall.example for list/VIP inquiries

Target Market(s)

Upscale top 40 crowd but want some cool and artsy like the examples included.

Font styles to use
Sans Serif

Requirements
Must have
• Harbor Logo
Nice to have
• Would be nice if the flyer can be incorporated later with DJ photos (sometimes we will add dj photos to pixagram etc). Would like a big city type of feel.
Should not have
• Nothing too sexual.

```html
<!DOCTYPE html>
<html lang="en">
<head>
<meta charset="utf-8">
<title>Harbor Fridays</title>
<link href="https://fonts.googleapis.com/css2?family=Bebas+Neue&family=Roboto:wght@400&display=swap" rel="stylesheet">
<style>
  :root{
    --page:#ffffff;
    --night:#121113;
    --night-mid:#3a3539;
    --orange:#f39a1e;
    --gold-light:#ffe08a;
    --gold:#d9902a;
    --gold-dark:#7a3f10;
    --olive:#b0b06a;
    --white:#ffffff;
    --glow-red:#c4162a;
    --glow-pink:#b0185e;
    --violet:#4a2457;
  }
  *{margin:0;padding:0;box-sizing:border-box}
  html,body{width:1200px;height:1200px;overflow:hidden;background:var(--page)}
  .flyer{
    position:absolute;left:306px;top:253px;width:587px;height:733px;overflow:hidden;
    background:radial-gradient(ellipse at 50% 45%, var(--night-mid) 0%, #242124 55%, var(--night) 100%);
    font-family:"Bebas Neue", "Oswald", sans-serif;color:var(--white);
  }
  .abs{position:absolute}
  .brand-mark{left:243px;top:69px;width:100px;height:100px;border-radius:50%;background:var(--olive)}
  .brand-name{left:0;width:587px;top:172px;text-align:center;font-size:48px;letter-spacing:6px;line-height:1}
  .frame{left:0;top:0;width:587px;height:420px}
  .title{
    left:0;width:587px;top:258px;text-align:center;font-size:78px;line-height:1;letter-spacing:1px;
    background:linear-gradient(180deg,var(--gold-light) 0%,var(--gold) 45%,var(--gold-dark) 60%,var(--gold) 100%);
    -webkit-background-clip:text;background-clip:text;color:transparent;
  }
  .skyline{left:192px;top:372px;width:210px;height:166px;
    background:linear-gradient(180deg,rgba(120,70,40,0) 0%,rgba(150,90,50,.55) 40%,#8a5530 100%)}
  .crowd{left:0;top:515px;width:587px;height:218px;
    background:
      linear-gradient(180deg,rgba(0,0,0,0) 0%,rgba(0,0,0,.35) 45%,#000 100%),
      linear-gradient(90deg,var(--glow-red) 0%,rgba(60,10,20,.6) 35%,rgba(40,5,20,.6) 65%,var(--glow-pink) 100%)}
  .rule{height:1.5px;background:var(--orange)}
  .date{left:194px;width:198px;top:542px;text-align:center;font-size:37px;color:var(--orange);line-height:1;word-spacing:6px}
  .lineup{left:0;width:587px;top:588px;text-align:center;font-size:30px;line-height:1}
  .lineup .name{color:var(--orange)}
  .lineup .sep{margin:0 14px;font-size:20px;vertical-align:middle}
  .floor{top:620px;font-family:"Roboto",sans-serif;font-size:11px;text-align:center;line-height:1}
  .address{left:0;width:587px;top:642px;text-align:center;font-size:19px;line-height:1}
  .note{left:0;width:587px;top:664px;text-align:center;font-family:"Roboto",sans-serif;font-size:11px;color:var(--orange)}
  .site{left:0;width:587px;top:681px;text-align:center;font-size:19px;line-height:1}
  .site .accent{color:var(--orange)}
</style>
</head>
<body>
<main class="flyer">
  <div class="abs crowd" role="img" aria-label="Silhouetted crowd with raised hands against red and magenta stage light"></div>

  <div class="abs brand-mark"></div>
  <div class="abs brand-name">HARBOR</div>

  <div class="abs skyline" role="img" aria-label="Illustrated city skyline with a clock tower in bronze tones"></div>

  <svg class="abs frame" viewBox="0 0 587 420" aria-hidden="true">
    <defs>
      <linearGradient id="goldLine" x1="0" x2="1">
        <stop offset="0" stop-color="#7a3f10"/>
        <stop offset=".45" stop-color="#ffd36a"/>
        <stop offset="1" stop-color="#7a3f10"/>
      </linearGradient>
    </defs>
    <polyline points="186,226 391,226 372,258" fill="none" stroke="var(--violet)" stroke-width="4"/>
    <polyline points="186,226 205,258" fill="none" stroke="var(--violet)" stroke-width="4"/>
    <polyline points="193,230 384,230 368,256" fill="none" stroke="url(#goldLine)" stroke-width="2.5"/>
    <polyline points="193,230 209,256" fill="none" stroke="url(#goldLine)" stroke-width="2.5"/>
    <polyline points="255,342 290,404 325,342" fill="none" stroke="var(--violet)" stroke-width="5"/>
    <polyline points="262,344 290,396 318,344" fill="none" stroke="url(#goldLine)" stroke-width="2.5"/>
  </svg>

  <div class="abs title">FRIDAYS</div>

  <div class="abs rule" style="left:194px;width:198px;top:538px"></div>
  <div class="abs date">FRI 1 MAY 2020</div>
  <div class="abs rule" style="left:194px;width:198px;top:578px"></div>

  <div class="abs lineup">DJ <span class="name">VORTAN</span><span class="sep">•</span><span class="name">DJ RUZO &amp; DJ TAV</span></div>
  <div class="abs floor" style="left:140px;width:120px">(club floor)</div>
  <div class="abs floor" style="left:290px;width:160px">(residents on the lounge floor)</div>
  <div class="abs rule" style="left:138px;width:310px;top:635px"></div>

  <div class="abs address">4217 MARLOW AVENUE SACRAMENTO</div>
  <div class="abs note">for list/VIP inquiries</div>
  <div class="abs site">WWW.<span class="accent">HARBORVENUEHALL</span>.EXAMPLE</div>
</main>
</body>
</html>
```